Wine Bottle Label for Cora Whitlow California Wine

This will be a wine bottle label. The wine is produced from grapes from our family farm. Images at bottom are some of same ones in high resolution

Cora Whitlow
Reserve Pinot Noir
Clarksburg 2023
Estate Grown (in cursive)

We would like to have a view from above, looking down from the levee there is a slough (wing of a river) running behind it, it looks down over vineyards, a big wood barn, a giant Oak Tree beyond the barn. There are beautiful sunsets there in the distance. Many birds fly over the vineyards including small black birds (as shown in one photo). Please use what you can from these suggestions to make a label. We will need a small image for back label and wording on it.

Other font styles liked:
• Wine bottle fonts

Requirements
Must have
• Wording mentioned . An Oak Tree with images of the vines and a sunset
Nice to have
• Flock of black birds flying in the sky

```html
<!DOCTYPE html>
<html lang="en">
<head>
<meta charset="utf-8">
<title>Cora Whitlow Reserve Pinot Noir Label</title>
<link rel="stylesheet" href="https://fonts.googleapis.com/css2?family=Libre+Baskerville:wght@700&family=Cinzel:wght@400;600&family=Pinyon+Script&family=Oswald:wght@400&display=swap">
<style>
  :root {
    --backdrop: #1c1c1d;
    --label-cream: #ecd3a3;
    --label-cream-light: #f3ddb1;
    --wine-red: #c8202c;
    --ink: #2a2420;
    --frame-copper: #b4683f;
    --vineyard-dark: #3b342c;
    --vineyard-mid: #7d7060;
  }
  * { box-sizing: border-box; margin: 0; padding: 0; }
  html, body {
    width: 1200px;
    height: 900px;
    overflow: hidden;
    background: var(--backdrop);
  }
  .stage {
    position: relative;
    width: 1200px;
    height: 900px;
    background: radial-gradient(ellipse at 50% 25%, #3a3a3b 0%, var(--backdrop) 60%);
  }
  .wine-label {
    position: absolute;
    left: 380px;
    top: 60px;
    width: 440px;
    height: 780px;
    background: linear-gradient(180deg, var(--label-cream-light) 0%, var(--label-cream) 100%);
    text-align: center;
    color: var(--ink);
  }
  .label-frame {
    position: absolute;
    inset: 10px;
    border: 2px solid var(--frame-copper);
    outline: 1px solid var(--frame-copper);
    outline-offset: -6px;
  }
  .winery-name {
    position: absolute;
    top: 118px;
    left: 0;
    right: 0;
    font-family: "Libre Baskerville", serif;
    font-weight: 700;
    font-size: 32px;
    color: var(--ink);
  }
  .vineyard-scene {
    position: absolute;
    top: 188px;
    left: 50px;
    width: 340px;
    height: 130px;
    border-radius: 50% 50% 40% 40% / 30% 30% 70% 70%;
    background: radial-gradient(ellipse at 50% 70%, var(--vineyard-dark) 0%, var(--vineyard-mid) 55%, rgba(236,211,163,0) 75%);
  }
  .reserve {
    position: absolute;
    top: 352px;
    left: 0;
    right: 0;
    font-family: "Cinzel", serif;
    font-weight: 400;
    font-size: 30px;
    color: var(--ink);
  }
  .varietal {
    position: absolute;
    top: 400px;
    left: 0;
    right: 0;
    font-family: "Cinzel", serif;
    font-weight: 600;
    font-size: 58px;
    color: var(--wine-red);
    letter-spacing: 1px;
  }
  .vintage {
    position: absolute;
    top: 482px;
    left: 0;
    right: 0;
    font-family: "Libre Baskerville", serif;
    font-weight: 700;
    font-size: 24px;
    color: var(--ink);
  }
  .appellation {
    position: absolute;
    top: 583px;
    left: 0;
    right: 0;
    font-family: "Cinzel", serif;
    font-weight: 400;
    font-size: 30px;
    letter-spacing: 1px;
    color: var(--ink);
  }
  .estate-grown {
    position: absolute;
    top: 618px;
    left: 0;
    right: 0;
    font-family: "Pinyon Script", cursive;
    font-size: 46px;
    color: var(--wine-red);
  }
  .label-footer {
    position: absolute;
    top: 710px;
    left: 32px;
    right: 32px;
    display: flex;
    justify-content: space-between;
    font-family: "Oswald", sans-serif;
    font-size: 17px;
    text-transform: uppercase;
    color: var(--ink);
  }
</style>
</head>
<body>
  <main class="stage">
    <section class="wine-label">
      <div class="label-frame"></div>
      <h1 class="winery-name">Cora Whitlow</h1>
      <div class="vineyard-scene" role="img" aria-label="Engraved illustration of vineyard rows rolling toward a barn and hills"></div>
      <p class="reserve">Reserve</p>
      <h2 class="varietal">Pinot Noir</h2>
      <p class="vintage">2023</p>
      <p class="appellation">CLARKSBURG</p>
      <p class="estate-grown">Estate Grown</p>
      <div class="label-footer">
        <span>Alc. 14.0% vol</span>
        <span>750ml</span>
      </div>
    </section>
  </main>
</body>
</html>
```